J & M Holloway Carpet & Gutter Cleaning

We clean carpets and have an environmentally friendly gutter machine that cleans out the guttering leaving no mess
Phone 0427816350
or 0438261907

Industry/Entity Type

Business

```html
<!DOCTYPE html>
<html lang="en">
<head>
<meta charset="utf-8">
<title>J &amp; M Holloway Carpet &amp; Gutter Cleaning – Business Card</title>
<link rel="stylesheet" href="https://fonts.googleapis.com/css2?family=Open+Sans:wght@600;700;800&display=swap">
<style>
  :root {
    --backdrop: #e9ecef;
    --card-white: #ffffff;
    --brand-blue: #1666a3;
    --band-red: #e3232b;
    --text-white: #ffffff;
    --mark-grey: #8a8d90;
    --machine-light: #d9d4c6;
    --machine-dark: #8f8872;
  }
  * { margin: 0; padding: 0; box-sizing: border-box; }
  html, body {
    width: 1200px;
    height: 751px;
    overflow: hidden;
    background: var(--backdrop);
    font-family: "Open Sans", Arial, sans-serif;
  }
  .business-card {
    position: absolute;
    left: 120px;
    top: 101px;
    width: 960px;
    height: 548px;
    border-radius: 40px;
    overflow: hidden;
    background: var(--card-white);
    box-shadow: 0 6px 24px rgba(0, 0, 0, 0.12);
  }
  .brand-name {
    position: absolute;
    left: 70px;
    top: 78px;
    color: var(--brand-blue);
    font-weight: 800;
    text-transform: uppercase;
    line-height: 1;
  }
  .brand-name__main {
    display: block;
    font-size: 66px;
    letter-spacing: 1px;
  }
  .brand-name__trade {
    display: block;
    margin-top: 10px;
    font-size: 38px;
    letter-spacing: 0.5px;
  }
  .brand-dot {
    position: absolute;
    left: 730px;
    top: 40px;
    width: 170px;
    height: 170px;
    border-radius: 50%;
    background: var(--mark-grey);
  }
  .service-band {
    position: absolute;
    left: 0;
    top: 300px;
    width: 100%;
    height: 44px;
    background: var(--band-red);
    color: var(--text-white);
    font-weight: 600;
    font-size: 23px;
    text-transform: uppercase;
    line-height: 44px;
  }
  .service-band__item { position: absolute; top: 0; }
  .service-band__item--carpet { left: 105px; }
  .service-band__divider { left: 390px; }
  .service-band__item--gutter { left: 440px; }
  .contact-panel {
    position: absolute;
    left: 0;
    top: 344px;
    width: 100%;
    height: 204px;
    background: var(--brand-blue);
  }
  .phone-list {
    position: absolute;
    left: 100px;
    top: 36px;
    list-style: none;
  }
  .phone-list__item {
    display: flex;
    align-items: center;
    height: 44px;
    margin-bottom: 28px;
    color: var(--text-white);
    font-weight: 700;
    font-size: 36px;
    letter-spacing: 1px;
  }
  .phone-list__icon {
    width: 30px;
    height: 30px;
    margin-right: 20px;
    flex: none;
  }
  .machine-photo {
    position: absolute;
    left: 620px;
    top: 360px;
    width: 300px;
    height: 170px;
    border-radius: 6px;
    background: linear-gradient(135deg, var(--machine-light), var(--machine-dark));
  }
</style>
</head>
<body>
  <main class="business-card">
    <h1 class="brand-name">
      <span class="brand-name__main">J &amp; M Holloway</span>
      <span class="brand-name__trade">Carpet &amp; Gutter Cleaning</span>
    </h1>
    <div class="brand-dot"></div>

    <div class="service-band">
      <span class="service-band__item service-band__item--carpet">Carpet Cleaning</span>
      <span class="service-band__item service-band__divider">|</span>
      <span class="service-band__item service-band__item--gutter">Gutter Machine Cleaning</span>
    </div>

    <section class="contact-panel">
      <ul class="phone-list">
        <li class="phone-list__item">
          <svg class="phone-list__icon" viewBox="0 0 30 30" aria-hidden="true">
            <rect width="30" height="30" rx="6" fill="#ffffff"/>
            <path d="M10 6 h4 l1 5 -2.5 2 a12 12 0 0 0 5 5 l2 -2.5 5 1 v4 a2 2 0 0 1 -2 2 A17 17 0 0 1 8 8 a2 2 0 0 1 2 -2z" fill="#1666a3"/>
          </svg>
          0427816350
        </li>
        <li class="phone-list__item">
          <svg class="phone-list__icon" viewBox="0 0 30 30" aria-hidden="true">
            <rect width="30" height="30" rx="6" fill="#ffffff"/>
            <path d="M10 6 h4 l1 5 -2.5 2 a12 12 0 0 0 5 5 l2 -2.5 5 1 v4 a2 2 0 0 1 -2 2 A17 17 0 0 1 8 8 a2 2 0 0 1 2 -2z" fill="#1666a3"/>
          </svg>
          0438261907
        </li>
      </ul>
    </section>

    <div class="machine-photo" role="img" aria-label="Photo of the gutter cleaning machine with its hose reels"></div>
  </main>
</body>
</html>
```